Short term Rentals Marketing agency needs Web design.

We Need a web design for our new company based in Calgary, AB. We are a International Luxury home sharing company (short term rental properties, Villas, Boutique Hotels, Bed & Breakfast, Realtors, Mortgage Brokers). We would like to see designs that look simple, modern and professional. Colors would be bold (red, black, white). The final design should communicate something welcoming, symbolize innovation, and growth. Our goal is to form partnerships with Real Estate, Property Management, Short term Rental Clients to make their lives easier and increase revenue. Vlto Harbor Co. offers a flexible and secure way to market our clients properties while maintaining client satisfaction and amazing customer service. We like how https://plumtrellisads.ca/ is interactive (when you scroll down, text gets larger). Other similar websites for Short Term Rentals is https://www.thekeyhavenfirm.com/, https://stayvorabnb.com/, https://www.nestquill.com/, https://www.roostfinch.com/about-us/, https://lodgewardens.com. We have attached our Logo.

Target Market(s)

short term rental properties, Villas, Boutique Hotels, Bed & Breakfast, Realtors, Mortgage Brokers, property owners

Industry/Entity Type

Real Estate

Coding

Coded - Design and coding required

Number of Pages Required

5+ page

Font styles to use
Sans Serif

Requirements
Must have
• Home Page, About Us page, How it works, Services, Contact us.

We like how https://plumtrellisads.ca/ is interactive (when you scroll down, text gets larger).

We have attached our Webcopy. We would like Call to Action Buttons where they're located in the copy and page.

Must have our Logo Colors.

Other similar websites for Short Term Rentals is https://www.thekeyhavenfirm.com/, https://stayvorabnb.com/, https://www.nestquill.com/, https://www.roostfinch.com/about-us/, https://lodgewardens.com.
Nice to have
• Catchy, Interactive Home page.

Should not have
• Should not be too cluttered

```html
<!DOCTYPE html>
<html lang="en">
<head>
<meta charset="utf-8">
<title>Vlto Harbor Co. — Our Services</title>
<link href="https://fonts.googleapis.com/css2?family=Playfair+Display:wght@700&family=Mulish:wght@400;500&display=swap" rel="stylesheet">
<style>
:root{
  --red:#e31e2a;
  --ink:#1e1e1e;
  --text:#2b2b2b;
  --muted:#6a6a6a;
  --line:#9a9a9a;
  --white:#ffffff;
  --sky-1:#cfe0f1;
  --sky-2:#eef4fa;
}
*{box-sizing:border-box;margin:0;padding:0}
html,body{width:1200px;height:2472px;overflow:hidden;background:var(--white)}
body{position:relative;font-family:"Mulish",sans-serif;color:var(--text)}
.abs{position:absolute}
.serif{font-family:"Playfair Display",serif;font-weight:700;color:var(--ink);letter-spacing:.5px}

.hero-photo{left:0;top:0;width:544px;height:573px;background:linear-gradient(135deg,#e9e6e3 0%,#d8cfc8 40%,#f2f1ef 100%)}
.brand{left:55px;top:24px;display:flex;align-items:center;gap:8px;font-size:18px;font-weight:500;color:var(--ink)}
.brand-mark{width:22px;height:22px;background:var(--red)}
.nav{top:37px;font-size:15px;color:var(--ink)}
.nav.current{color:var(--muted)}
.nav-cta{left:999px;top:28px;width:149px;height:37px;border:1px solid var(--ink);font-size:15px;display:flex;align-items:center;justify-content:center;color:var(--ink)}

.intro-title{left:626px;top:196px;font-size:36px}
.intro-copy{left:626px;top:266px;width:430px;font-size:17px;line-height:24px}
.scroll{left:626px;top:443px;font-size:15px;color:var(--red);display:flex;align-items:center;gap:10px}
.scroll::before{content:"";width:33px;height:1px;background:var(--red)}

.card{border:1px solid var(--line);border-radius:3px;padding:16px 20px}
.card svg{display:block;margin-bottom:12px}
.card h3{font-size:23px;line-height:26px;margin-bottom:12px}
.card p{font-size:16.6px;line-height:23.8px}

.contact-band{left:0;top:1570px;width:1200px;height:508px;background:linear-gradient(180deg,var(--sky-1),var(--sky-2))}
.contact-photo{left:660px;top:1595px;width:540px;height:483px;background:linear-gradient(160deg,#9fbdd8 0%,#7fa3c5 50%,#b9d0e4 100%);clip-path:polygon(40% 0,60% 4%,100% 40%,100% 100%,5% 100%)}
.contact-title{left:55px;top:1638px;font-size:38px}
.field{border:1px solid #5e6b78;font-size:15px;color:var(--ink);padding:10px 15px;background:transparent}
.agree{left:55px;top:1977px;font-size:13px;color:var(--ink)}
.send{left:407px;top:1967px;width:170px;height:37px;background:var(--red);color:var(--white);font-size:16px;display:flex;align-items:center;justify-content:center}

.foot-title{top:2162px;font-size:24px;font-weight:400;font-family:"Playfair Display",serif;color:var(--ink)}
.foot-list{top:2222px;list-style:none;font-size:17px;line-height:32.5px;color:var(--ink)}
.social{left:859px;top:2224px;display:flex;gap:21px}
.social span{width:24px;height:24px;border-radius:50%;background:var(--ink)}
.social span:first-child{background:var(--red)}
.rule{left:0;top:2374px;width:1200px;height:1px;background:#cfcfcf}
.legal{top:2405px;font-size:17px;color:var(--muted)}
</style>
</head>
<body>
<div class="abs hero-photo" role="img" aria-label="Photo of a hand signing a rental agreement at a desk"></div>
<div class="abs brand"><span class="brand-mark"></span>Vlto Harbor Co.</div>
<div class="abs nav" style="left:626px">About us</div>
<div class="abs nav current" style="left:732px">Our Services</div>
<div class="abs nav" style="left:864px">How it works</div>
<div class="abs nav-cta">Contact Us</div>

<h1 class="abs serif intro-title">Our Services</h1>
<p class="abs intro-copy">As an innovative rental management and marketing agency, we don’t just do the bare minimum when it comes to our clients – we go above and beyond what is expected of us. Our friendly and welcoming team of experts is dedicated to meeting every one of your needs and exceeding your expectations. Here are some of our amazing offers:</p>
<div class="abs scroll">Scroll down ⌄</div>

<div class="abs card" style="left:55px;top:648px;width:348px;height:403px">
  <svg width="36" height="50" viewBox="0 0 36 50" fill="none" stroke="#222" stroke-width="2"><rect x="2" y="2" width="32" height="46" rx="3"/><path d="M10 24l8-7 8 7v9H10z" stroke="#e31e2a"/></svg>
  <h3 class="serif">Import and Export Auto Ratings</h3>
  <p>You can easily update or change your listings’ prices from one place and automatically import/export those changes to all your other platforms.</p>
</div>
<div class="abs card" style="left:427px;top:648px;width:348px;height:403px">
  <svg width="52" height="50" viewBox="0 0 52 50" fill="none" stroke="#222" stroke-width="2"><path d="M4 4v44"/><rect x="4" y="6" width="46" height="18" rx="2"/><path d="M12 20v-6l5-4 5 4v6" stroke="#e31e2a"/></svg>
  <h3 class="serif">Direct Bookings</h3>
  <p>Vlto Harbor Co. will boost your revenue by listing your property on different rental platforms for your short-term rental properties on which your clients can make direct bookings.</p>
</div>
<div class="abs card" style="left:798px;top:648px;width:348px;height:403px">
  <svg width="50" height="50" viewBox="0 0 50 50" fill="none" stroke="#222" stroke-width="2"><rect x="2" y="2" width="32" height="46" rx="2"/><path d="M8 28h20M8 34h16M8 40h12"/><path d="M10 18v-6l6-5 6 5v6" stroke="#e31e2a"/><circle cx="38" cy="38" r="9" stroke="#e31e2a"/><path d="M34 38l3 3 6-6" stroke="#e31e2a"/></svg>
  <h3 class="serif">Powerful Reporting</h3>
  <p>Keep track of every single transaction date and customer detail, as well as rates and cleaning fees,tax amounts, and more - thanks to our custom property reports. These reports will not onlybenchmark your properties, but also help you stay updated on any potential changes.</p>
</div>

<div class="abs card" style="left:55px;top:1086px;width:348px;height:406px">
  <svg width="48" height="48" viewBox="0 0 48 48" fill="none" stroke="#222" stroke-width="2"><path d="M4 44h40M8 44V26l14-12 14 12v18"/><rect x="18" y="32" width="8" height="12"/><circle cx="38" cy="8" r="4" stroke="#e31e2a"/></svg>
  <h3 class="serif">Cleaning and Organization</h3>
  <p>We can manage and oversee any work-orders, set cleaning tasks, and give you real-time updates thanks to our integrated calendar system.</p>
</div>
<div class="abs card" style="left:427px;top:1086px;width:348px;height:406px">
  <svg width="54" height="48" viewBox="0 0 54 48" fill="none" stroke="#222" stroke-width="2"><path d="M20 16v-6l7-6 7 6v6" stroke="#e31e2a"/><path d="M2 26l10-6 10 4 8-4 12 0 10 6M12 34l10 8 8-4 12-8"/></svg>
  <h3 class="serif">Customer Communication</h3>
  <p>We will keep an open line of communication with your clients by managing their booking process, sending them check-in instructions, communicating with them during their stay, sending them ‘thank you’ messages when they leave, and requesting property reviews. We will help you create a customer experience that will keep them coming back every time.</p>
</div>
<div class="abs card" style="left:798px;top:1086px;width:348px;height:406px">
  <svg width="48" height="48" viewBox="0 0 48 48" fill="none" stroke="#222" stroke-width="2"><rect x="2" y="2" width="30" height="44" rx="2"/><path d="M8 28h18M8 34h14M8 40h10"/><path d="M9 18v-6l6-5 6 5v6" stroke="#e31e2a"/><circle cx="37" cy="37" r="9" stroke="#e31e2a"/><path d="M33 37l3 3 6-6" stroke="#e31e2a"/></svg>
  <h3 class="serif">Calendar Adjustments</h3>
  <p>When you adjust your calendars, we’ll ensure the information is changed on every single platform your property is listed on - thanks to calendar cross-synchronization. This includes customizations regarding different events, seasons, dates, and more.</p>
</div>

<div class="abs contact-band"></div>
<div class="abs contact-photo" role="img" aria-label="Photo of a modern glass apartment tower against the sky"></div>
<h2 class="abs serif contact-title">Contact Us Today</h2>
<div class="abs field" style="left:55px;top:1713px;width:248px;height:40px">Name</div>
<div class="abs field" style="left:329px;top:1713px;width:248px;height:40px">Email</div>
<div class="abs field" style="left:55px;top:1769px;width:522px;height:40px">Phone Number</div>
<div class="abs field" style="left:55px;top:1822px;width:522px;height:129px">Message</div>
<div class="abs agree">By Sending I agree to terms and conditions</div>
<div class="abs send">Send</div>

<h4 class="abs foot-title" style="left:57px">Company</h4>
<ul class="abs foot-list" style="left:57px"><li>About Us</li><li>Services</li><li>How it works</li><li>Contact</li></ul>
<h4 class="abs foot-title" style="left:332px">Inspiration</h4>
<ul class="abs foot-list" style="left:332px"><li>Blog</li><li>Gallary</li><li>Testimonials</li></ul>
<h4 class="abs foot-title" style="left:614px">Help</h4>
<ul class="abs foot-list" style="left:614px"><li>FAQS</li><li>Customers support</li></ul>
<h4 class="abs foot-title" style="left:859px">Social media</h4>
<div class="abs social"><span></span><span></span><span></span></div>

<div class="abs rule"></div>
<div class="abs legal" style="left:55px">Privacy Policy &nbsp;&nbsp; Customer Agreement</div>
<div class="abs legal" style="right:52px">© 2020 All Rights Reserved</div>
</body>
</html>
```